Minimalist, Flat(Matte) design for a Beef Jerky packaging company. No bullshit company looking for a

Need a packaging design for a new Beef Jerky product(in English). The name of the company is 'Velmor' and thus the packaging should reflect the bullish, tough, and simple nature of the beef jerky product. The finished product should communicate simplicity, minimalism, yet toughness and strength.

The logo should be simple, with a minimal number of colors , and should be either all white/cream, or have some red as well. Main colors should be white, cream, tinted red, and matte black. I think 4 colors max would be best. The closest example to an existing package style would be Korvanti Dusk clove cigarettes( image attached).

It will be on a matte black standing pouch package. See image for package type. Package dimensions:

Dimension: Width x Gusset x Height
INCH : 5.125" (W) x 3.125" (G) x 8.125" (H)
MILLIMETER : 130mm (W) x 80mm (G) x 205mm (H)

I don't have anything totally specific so artistic liberty is encouraged, provided the colors are kept to a minimum and looks consistent with the simple nature of the brand and the matte black packaging.

Also attached an existing beef jerky package with a similar style to what we're looking for.

Industry/Entity Type

It Company

Colors
f59195
ffffff

Requirements
Must have
• Low contrast, flat and minimalist design.
Should not have
• A complicated design with many colors. Gawdy/flashy design. Bright colors. High contrast.

```html
<!DOCTYPE html>
<html lang="en">
<head>
<meta charset="utf-8">
<title>Velmor Beef Jerky – Garlic, Lime &amp; Cilantro</title>
<link rel="stylesheet" href="https://fonts.googleapis.com/css2?family=Barlow+Semi+Condensed:wght@500;600;700;800&display=swap">
<style>
  :root {
    --pouch-black: #0a0b0c;
    --tinted-red: #e69094;
    --cream-white: #ffffff;
    --soft-grey: #dcdcdc;
    --edge-grey: #4a4a4a;
  }
  * { margin: 0; padding: 0; box-sizing: border-box; }
  html, body {
    width: 761px;
    height: 1200px;
    overflow: hidden;
    background: var(--pouch-black);
  }
  .pouch-front {
    position: relative;
    width: 761px;
    height: 1200px;
    background: var(--pouch-black);
    border: 1px solid var(--edge-grey);
    font-family: "Barlow Semi Condensed", "Arial Narrow", sans-serif;
    overflow: hidden;
  }
  .sweep-lines {
    position: absolute;
    left: 0;
    top: 0;
    width: 761px;
    height: 1200px;
  }
  .sweep-lines path {
    fill: none;
    stroke: var(--tinted-red);
  }
  .line {
    position: absolute;
    left: 0;
    width: 100%;
    text-align: center;
    line-height: 1;
    white-space: nowrap;
  }
  .tagline {
    top: 422px;
    font-size: 25px;
    font-weight: 600;
    letter-spacing: 1.5px;
    color: var(--soft-grey);
  }
  .tagline .dot {
    display: inline-block;
    width: 17px;
    height: 17px;
    margin: 0 26px 2px;
    border-radius: 50%;
    background: var(--tinted-red);
    vertical-align: middle;
  }
  .brand-name {
    top: 518px;
    font-size: 126px;
    font-weight: 800;
    letter-spacing: 14px;
    padding-left: 14px;
    color: var(--tinted-red);
  }
  .flavour {
    top: 751px;
    font-size: 30px;
    font-weight: 600;
    letter-spacing: 0.5px;
    color: var(--cream-white);
  }
  .product-type {
    top: 792px;
    font-size: 64px;
    font-weight: 800;
    letter-spacing: 4px;
    color: var(--cream-white);
  }
  .net-weight {
    top: 1059px;
    font-size: 22px;
    font-weight: 700;
    color: var(--cream-white);
  }
</style>
</head>
<body>
  <main class="pouch-front">
    <svg class="sweep-lines" viewBox="0 0 761 1200" aria-hidden="true">
      <g class="sweep-top">
        <path d="M -30 282 Q 380 138 791 282" stroke-width="2"/>
        <path d="M -30 310 Q 380 172 791 310" stroke-width="7"/>
        <path d="M -30 330 Q 380 214 791 330" stroke-width="2"/>
        <path d="M -30 352 Q 380 244 791 352" stroke-width="2"/>
      </g>
      <g class="sweep-bottom">
        <path d="M -30 834 Q 380 922 791 834" stroke-width="2"/>
        <path d="M -30 862 Q 380 982 791 862" stroke-width="7"/>
        <path d="M -30 892 Q 380 1000 791 892" stroke-width="2"/>
        <path d="M -30 912 Q 380 1020 791 912" stroke-width="2"/>
      </g>
    </svg>

    <p class="line tagline">HAND-CRAFTED<span class="dot"></span>SMALL BATCH</p>
    <h1 class="line brand-name">VELMOR</h1>
    <p class="line flavour">GARLIC, LIME &amp; CILANTRO</p>
    <h2 class="line product-type">BEEF JERKY</h2>
    <p class="line net-weight">NET WT. 3 OZ</p>
  </main>
</body>
</html>
```